We need a design for business cards for our new company. We are a resident safety and security company company that focuses on senior living communities. we provide Nurse call, Access control, CCTV, Wired and wireless network infrastructure, Wander Management, and much more!

Our logo is the circuit board shield. Representing our high tech security solutions. I would like the business card to bring the same theme with perhaps some circuit board traces around the card similar to our logo

```html
<!DOCTYPE html>
<html lang="en">
<head>
<meta charset="utf-8">
<title>ElderNova Business Cards</title>
<link rel="stylesheet" href="https://fonts.googleapis.com/css2?family=Lora:ital,wght@0,400;0,700;1,400&display=swap">
<style>
  :root {
    --page-bg: #e9ecef;
    --card-white: #ffffff;
    --card-grey: #e6e8ea;
    --blue-deep: #2763b8;
    --blue-mid: #2f8fd0;
    --blue-light: #44b8e0;
    --blue-text: #2a6fc4;
    --blue-name: #3fb0e3;
    --grey-text: #6c7278;
    --dark-text: #3b4148;
    --white: #ffffff;
  }
  * { box-sizing: border-box; margin: 0; padding: 0; }
  html, body { width: 1200px; height: 917px; overflow: hidden; }
  body {
    background: var(--page-bg);
    font-family: "Lora", Georgia, serif;
    position: relative;
  }
  .card {
    position: absolute;
    border-radius: 4px;
    box-shadow: 0 8px 24px rgba(0,0,0,0.18);
    overflow: hidden;
  }

  /* Front card */
  .card-front {
    left: 110px; top: 170px;
    width: 330px; height: 578px;
    background: linear-gradient(160deg, var(--card-white) 0%, var(--card-grey) 100%);
  }
  .brand {
    position: absolute; top: 120px; left: 0; right: 0;
    display: flex; align-items: center; justify-content: center; gap: 10px;
  }
  .brand-dot {
    width: 18px; height: 18px; border-radius: 50%;
    background: var(--blue-mid);
  }
  .brand-name {
    font-size: 38px; font-weight: 400; color: var(--blue-text);
    letter-spacing: 0.5px;
  }
  .person { position: absolute; top: 220px; left: 0; right: 0; text-align: center; }
  .person-name { font-size: 25px; font-weight: 700; color: var(--blue-name); }
  .person-title { font-size: 13px; color: var(--grey-text); letter-spacing: 1px; margin-top: 2px; }

  .contacts { position: absolute; top: 300px; left: 30px; right: 30px; }
  .contact-divider {
    position: relative; height: 22px;
    display: flex; align-items: center; justify-content: center;
  }
  .contact-divider::before {
    content: ""; position: absolute; left: 0; right: 0; top: 50%;
    border-top: 1px solid var(--blue-light);
  }
  .contact-icon {
    position: relative; width: 22px; height: 22px; border-radius: 50%;
    background: var(--blue-mid); display: flex; align-items: center; justify-content: center;
  }
  .contact-text {
    text-align: center; font-size: 17px; color: var(--dark-text);
    padding: 6px 0 8px;
  }
  .contact-email { font-size: 15px; }

  .web-band {
    position: absolute; left: 0; right: 0; bottom: 0; height: 96px;
    background: linear-gradient(180deg, var(--blue-mid) 0%, var(--blue-deep) 100%);
    display: flex; align-items: center; justify-content: center;
  }
  .web-band::before {
    content: ""; position: absolute; left: 0; right: 0; top: 6px;
    border-top: 1px solid rgba(255,255,255,0.45);
  }
  .web-address { color: var(--white); font-size: 18px; letter-spacing: 0.5px; }

  /* Back card */
  .card-back {
    left: 520px; top: 294px;
    width: 578px; height: 330px;
    background: linear-gradient(135deg, var(--blue-deep) 0%, var(--blue-mid) 55%, var(--blue-light) 100%);
    color: var(--white);
    text-align: center;
  }
  .back-name {
    position: absolute; top: 70px; left: 0; right: 0;
    font-size: 60px; font-weight: 400; letter-spacing: 2px;
  }
  .provide-row {
    position: absolute; top: 170px; left: 0; right: 0;
    display: flex; align-items: center; justify-content: center; gap: 14px;
  }
  .provide-rule { width: 34px; border-top: 2px solid var(--white); }
  .provide-label { font-size: 14px; font-weight: 700; letter-spacing: 1.5px; }
  .services {
    position: absolute; top: 210px; left: 30px; right: 30px;
    font-size: 13px; font-style: italic; line-height: 1.7;
  }
</style>
</head>
<body>
  <section class="card card-front">
    <div class="brand">
      <span class="brand-dot"></span>
      <span class="brand-name">ElderNova</span>
    </div>
    <div class="person">
      <div class="person-name">Mark Hollis</div>
      <div class="person-title">President</div>
    </div>
    <div class="contacts">
      <div class="contact-divider">
        <span class="contact-icon">
          <svg width="12" height="12" viewBox="0 0 24 24" aria-hidden="true"><path fill="#fff" d="M6.6 10.8a15.1 15.1 0 0 0 6.6 6.6l2.2-2.2c.3-.3.7-.4 1-.2 1.1.4 2.3.6 3.6.6.6 0 1 .4 1 1V20c0 .6-.4 1-1 1A17 17 0 0 1 3 4c0-.6.4-1 1-1h3.5c.6 0 1 .4 1 1 0 1.3.2 2.5.6 3.6.1.3 0 .7-.2 1z"/></svg>
        </span>
      </div>
      <div class="contact-text">(555) 214-7730</div>
      <div class="contact-divider">
        <span class="contact-icon">
          <svg width="12" height="12" viewBox="0 0 24 24" aria-hidden="true"><rect x="6" y="2" width="12" height="20" rx="2" fill="none" stroke="#fff" stroke-width="2"/><circle cx="12" cy="18" r="1.3" fill="#fff"/></svg>
        </span>
      </div>
      <div class="contact-text">(555) 388-0142</div>
      <div class="contact-divider">
        <span class="contact-icon">
          <svg width="12" height="12" viewBox="0 0 24 24" aria-hidden="true"><rect x="3" y="5" width="18" height="14" rx="1" fill="none" stroke="#fff" stroke-width="2"/><path d="M3 6l9 7 9-7" fill="none" stroke="#fff" stroke-width="2"/></svg>
        </span>
      </div>
      <div class="contact-text contact-email">Mark@ElderNova.com</div>
    </div>
    <div class="web-band">
      <span class="web-address">www.ElderNova.com</span>
    </div>
  </section>

  <section class="card card-back">
    <div class="back-name">ElderNova</div>
    <div class="provide-row">
      <span class="provide-rule"></span>
      <span class="provide-label">WE PROVIDE</span>
      <span class="provide-rule"></span>
    </div>
    <p class="services">
      Nurse call | Access control | CCTV | Wired and wireless network infrastructure<br>
      Wander Management | and much more!
    </p>
  </section>
</body>
</html>
```